Flyer design for the Harvest Lantern Summit 2019 (HALSUM)

Design a flyer for our annual conference with basic information about the conference: conference logo and year, Conference name: Harvest Lantern Summit Location: Talbot Community Center (Downtown Portland)482 Wexley Street, Portland, ME 04109, Date: August 8th, 9th, 10th and 11th, 2019Start time 7:00PMI would like the following three words added to the flyer. These words describe the vision of the conference: Prophetic, Fire, Overflow,

Contact info:
Website: www.vostel.org
Phone: 207 555 3184
Email: contact@meadowcrest.org

Target Market(s)

Young adults living in the United States

Industry/Entity Type

Religious

Font styles to use
Sans Serif

Colors

Designer to choose colors to be used in the design.

Requirements
Must have
• HALSUM must logo standout, the reader should be able to take a quick look and find key info,
Should not have
• Cross image, church image

```html
<!DOCTYPE html>
<html lang="en">
<head>
<meta charset="UTF-8">
<title>Harvest Lantern Summit 2019 Flyer</title>
<link href="https://fonts.googleapis.com/css2?family=Arimo:wght@400;700&family=Cinzel:wght@700;900&family=Alfa+Slab+One&display=swap" rel="stylesheet">
<style>
  :root {
    --page-bg: #2b2a29;
    --flyer-dark: #120f0d;
    --photo-warm: #c2611c;
    --photo-glow: #ffb347;
    --band-black: rgba(0, 0, 0, 0.82);
    --text-white: #ffffff;
    --logo-blue: #1f7fcf;
    --logo-orange: #f08a1c;
    --accent-red: #e3161d;
    --rule-grey: rgba(255, 255, 255, 0.45);
  }
  html, body {
    margin: 0;
    padding: 0;
    width: 1200px;
    height: 800px;
    overflow: hidden;
    background: var(--page-bg);
  }
  .canvas {
    position: relative;
    width: 1200px;
    height: 800px;
  }
  .flyer {
    position: absolute;
    left: 332px;
    top: 20px;
    width: 536px;
    height: 760px;
    overflow: hidden;
    background: var(--flyer-dark);
    box-shadow: 0 10px 30px rgba(0,0,0,0.5);
  }
  .flyer__photo {
    position: absolute;
    inset: 0;
    background:
      radial-gradient(ellipse 90px 120px at 195px 600px, rgba(255,220,140,0.95), rgba(255,160,60,0.55) 45%, rgba(255,140,40,0) 100%),
      radial-gradient(ellipse 60px 40px at 380px 470px, rgba(255,170,60,0.5), rgba(255,170,60,0) 100%),
      radial-gradient(ellipse 40px 30px at 470px 400px, rgba(255,170,60,0.4), rgba(255,170,60,0) 100%),
      linear-gradient(180deg, #1a1613 0%, #231b16 35%, #2a1c12 62%, #6e3512 80%, var(--photo-warm) 92%, #8a3f12 100%);
  }
  .logo {
    position: absolute;
    top: 52px;
    left: 0;
    width: 100%;
    text-align: center;
  }
  .logo__name {
    font-family: 'Arimo', sans-serif;
    font-weight: 700;
    font-size: 48px;
    letter-spacing: 1px;
    color: var(--logo-blue);
    line-height: 1;
  }
  .logo__year {
    display: flex;
    align-items: center;
    justify-content: center;
    gap: 8px;
    margin-top: 4px;
    font-family: 'Arimo', sans-serif;
    font-weight: 700;
    font-size: 20px;
    letter-spacing: 10px;
    color: var(--logo-orange);
  }
  .logo__rule {
    width: 60px;
    height: 2px;
    background: var(--logo-orange);
  }
  .title {
    position: absolute;
    top: 150px;
    left: 0;
    width: 100%;
    margin: 0;
    text-align: center;
    font-family: 'Cinzel', serif;
    font-weight: 900;
    color: var(--text-white);
    line-height: 1.05;
  }
  .title__line { display: block; font-size: 54px; }
  .title__line--accent { color: var(--accent-red); font-size: 50px; }
  .vision {
    position: absolute;
    top: 342px;
    left: 0;
    width: 100%;
    text-align: center;
    font-family: 'Alfa Slab One', serif;
    font-size: 19px;
    letter-spacing: 0.5px;
    color: var(--text-white);
  }
  .venue {
    position: absolute;
    top: 382px;
    left: 0;
    width: 100%;
    padding: 16px 0;
    background: var(--band-black);
    text-align: center;
    font-family: 'Arimo', sans-serif;
    font-size: 20px;
    line-height: 1.35;
    color: var(--text-white);
  }
  .schedule {
    position: absolute;
    top: 540px;
    left: 322px;
    width: 170px;
    padding: 12px 0;
    border-top: 1px solid var(--rule-grey);
    border-bottom: 1px solid var(--rule-grey);
    text-align: center;
    font-family: 'Arimo', sans-serif;
    color: var(--text-white);
  }
  .schedule__dates { font-size: 20px; line-height: 1.3; }
  .schedule__time { font-size: 24px; margin-top: 14px; }
</style>
</head>
<body>
  <main class="canvas">
    <article class="flyer">
      <div class="flyer__photo" role="img" aria-label="Photograph of a lit candle in a glass holder on a wooden table in a dim room"></div>

      <header class="logo">
        <div class="logo__name">HALSUM</div>
        <div class="logo__year"><span class="logo__rule"></span>2019<span class="logo__rule"></span></div>
      </header>

      <h1 class="title">
        <span class="title__line">Harvest</span>
        <span class="title__line title__line--accent">Lantern</span>
        <span class="title__line">Summit</span>
      </h1>

      <p class="vision">PROPHETIC, FIRE, OVERFLOW</p>

      <section class="venue">
        Talbot Community Center<br>
        (Downtown Portland)<br>
        482 Wexley Street, Portland, ME 04109,
      </section>

      <section class="schedule">
        <div class="schedule__dates">August<br>8th, 9th, 10th<br>and 11th,<br>2019</div>
        <div class="schedule__time">7:00 PM</div>
      </section>
    </article>
  </main>
</body>
</html>
```